Business Card and Letterhead for new company Vardel GreenWorks, Inc.

Vardel GreenWorks, Inc., an engineering and construction firm that provides services for solid waste landfill gas systems, needs a business card and letterhead. We recently had a logo designed but we are open to some tweaks to logo design and color scheme. Generally, we like "earthy" color tones - greens, browns, oranges. This is a sister company - www.talvoriengineering.example.

Target Market(s)

Solid waste landfill companies - Brindle Disposal, Halcott Hauling, etc.

Industry/Entity Type

Engineering and Construction

Contact Information for Business Card

Name, Title, email, mobile phone, work phone, website. Potential list of services for back of card: LFG Engineering and Design, GCCS Planning and Operational Consulting, Compliance Monitoring and Reporting, Routine Operations & Maintenance, Nonroutine O&M, Construction Management, Construction QA, GCCS Construction

Font styles to use
Sans Serif

Requirements
Must have
• Logo, pertinent information, maybe a tagline (still in development)
Nice to have
• For back of card, considering an engineering scale (attached for another business of ours), but want to look at other options, alternatives. Like the idea of the back of card to have some utility (scale, unit conversion info, list of services) but willing to consider lots of options.
Should not have
• Needs to have a professional (engineering) and technical look, not cartoonish.

```html
<!DOCTYPE html>
<html lang="en">
<head>
<meta charset="utf-8">
<title>Vardel GreenWorks, Inc. – Business Card</title>
<link rel="stylesheet" href="https://fonts.googleapis.com/css2?family=Montserrat:wght@500;600;700;800&family=Roboto:wght@400;500&display=swap">
<style>
  :root {
    --page: #e9e6e1;
    --ink: #1d1d1d;
    --white: #ffffff;
    --green: #76b535;
    --blue: #2190b3;
    --grey: #8a8a8c;
    --flame: #f28a1e;
    --sky-top: #b9a6d8;
    --sky-pink: #f09bb4;
    --sky-orange: #f7a06c;
    --ground: #050505;
  }
  * { box-sizing: border-box; margin: 0; padding: 0; }
  html, body { width: 1200px; height: 900px; overflow: hidden; background: var(--page); }
  .canvas { position: relative; width: 1200px; height: 900px; }

  .card {
    position: absolute;
    width: 720px;
    height: 410px;
    overflow: hidden;
    box-shadow: 0 10px 28px rgba(0,0,0,.22);
  }

  /* Back of card */
  .card-back { left: 60px; top: 34px; background: var(--ground); }
  .back-photo {
    position: absolute; inset: 0;
    background:
      linear-gradient(180deg, var(--sky-top) 0%, var(--sky-pink) 22%, var(--sky-orange) 42%, #e58a78 50%, #3a1e1c 56%, var(--ground) 62%, var(--ground) 100%);
  }
  .back-name {
    position: absolute; left: 70px; top: 46px;
    font-family: "Montserrat", sans-serif; font-weight: 800;
    font-size: 62px; letter-spacing: 2px; line-height: 1;
    color: rgba(120,120,128,.55);
  }
  .back-name-dot {
    position: absolute; left: 30px; top: 56px;
    width: 34px; height: 34px; border-radius: 50%;
    background: rgba(120,120,128,.45);
  }
  .services {
    position: absolute; list-style: none;
    font-family: "Montserrat", sans-serif; font-weight: 500;
    color: var(--white);
  }
  .services li { position: relative; padding-left: 18px; }
  .services li::before {
    content: ""; position: absolute; left: 0; top: 50%;
    width: 9px; height: 9px; margin-top: -5px;
    border-radius: 50%; background: var(--flame);
  }
  .services-main { left: 40px; top: 272px; font-size: 17px; line-height: 27px; }
  .services-extra { left: 440px; top: 232px; font-size: 14px; line-height: 23px; }

  /* Front of card */
  .card-front { left: 420px; top: 466px; background: var(--white); }
  .front-waves { position: absolute; inset: 0; }
  .holder { position: absolute; left: 48px; top: 70px; }
  .holder-name {
    font-family: "Montserrat", sans-serif; font-weight: 800;
    font-size: 25px; letter-spacing: 1.5px; text-transform: uppercase;
    color: var(--green);
  }
  .holder-title {
    font-family: "Montserrat", sans-serif; font-weight: 600;
    font-size: 14px; letter-spacing: 2.5px; text-transform: uppercase;
    color: var(--blue); margin-top: 2px;
  }
  .brand { position: absolute; left: 360px; top: 58px; display: flex; align-items: center; gap: 12px; }
  .brand-mark { width: 44px; height: 44px; border-radius: 50%; background: var(--green); flex: none; }
  .brand-name {
    font-family: "Montserrat", sans-serif; font-weight: 700;
    font-size: 26px; line-height: 1.05; color: var(--green);
  }
  .contact { position: absolute; left: 58px; top: 196px; list-style: none;
    font-family: "Roboto", sans-serif; font-size: 20px; color: var(--ink); }
  .contact li { display: flex; align-items: center; gap: 10px; height: 28px; }
  .contact svg { width: 18px; height: 18px; flex: none; }
  .website {
    position: absolute; right: 40px; bottom: 60px;
    font-family: "Roboto", sans-serif; font-size: 16px; color: var(--white);
  }
</style>
</head>
<body>
<main class="canvas">

  <section class="card card-back" aria-label="Back of business card">
    <div class="back-photo" role="img" aria-label="Photograph of a pink and orange sunset sky over a landfill site with an excavator silhouette"></div>
    <span class="back-name-dot"></span>
    <div class="back-name">Vardel GreenWorks</div>
    <ul class="services services-main">
      <li>LFG Engineering and Design</li>
      <li>GCCS Planning and Operational Consulting</li>
      <li>Compliance Monitoring and Reporting</li>
      <li>Routine Operations &amp; Maintenance</li>
    </ul>
    <ul class="services services-extra">
      <li>Nonroutine O&amp;M</li>
      <li>Construction Management</li>
      <li>Construction QA</li>
      <li>GCCS Construction</li>
    </ul>
  </section>

  <section class="card card-front" aria-label="Front of business card">
    <svg class="front-waves" viewBox="0 0 720 410" preserveAspectRatio="none" aria-hidden="true">
      <path fill="var(--blue)" d="M0 318 C 200 338, 380 300, 560 188 C 410 300, 230 352, 0 346 Z"/>
      <path fill="var(--green)" d="M0 352 C 230 360, 430 300, 720 150 L720 410 L0 410 Z"/>
    </svg>

    <div class="holder">
      <div class="holder-name">Marlow Kestin</div>
      <div class="holder-title">Managing Director</div>
    </div>

    <div class="brand">
      <span class="brand-mark"></span>
      <div class="brand-name">Vardel<br>GreenWorks</div>
    </div>

    <ul class="contact">
      <li>
        <svg viewBox="0 0 24 24"><path fill="var(--green)" d="M6.6 10.8a15 15 0 0 0 6.6 6.6l2.2-2.2c.3-.3.7-.4 1-.2 1.1.4 2.3.6 3.6.6.6 0 1 .4 1 1V20c0 .6-.4 1-1 1A17 17 0 0 1 3 4c0-.6.4-1 1-1h3.5c.6 0 1 .4 1 1 0 1.3.2 2.5.6 3.6.1.3 0 .7-.2 1z"/></svg>
        044-555 010 247
      </li>
      <li>
        <svg viewBox="0 0 24 24"><rect x="6" y="2" width="12" height="20" rx="2" fill="none" stroke="var(--green)" stroke-width="2"/><circle cx="12" cy="18" r="1.2" fill="var(--green)"/></svg>
        044-555 010 318
      </li>
      <li>
        <svg viewBox="0 0 24 24"><rect x="2" y="5" width="20" height="14" fill="var(--green)"/><path d="M2 5 L12 13 L22 5" fill="none" stroke="var(--white)" stroke-width="1.6"/></svg>
        info@vardelgreenworks.example
      </li>
    </ul>

    <div class="website">www.vardelgreenworks.example</div>
  </section>

</main>
</body>
</html>
```